Create banners that convert viewers into buyers!

We provide Online Marketing Solutions for small to medium size businesses from web design, Local SEO, Pay-Per-Click, Social Media and Content Marketing. We've been helping local businesses since 2009 and offer a very high level of service that is rarely matched.

Really like to stay colors of logo like banner ad ideas 2 sample.

Would also like to use a photo of a responsive web design as attached image. (you may use a different layout as image provided may be to big for some dimensions)

Sizes needed:
728x90
300x250
480x60

Add Slogan: We Drive Traffic & Phone Calls!

Slogan: We Drive Phone Calls & Conversions

Target Market(s)

Small to Medium Size businesses: Main businesses we work with are Home Improvement, Lawyers & Physicians

Industry/Entity Type

Marketing

```html
<!DOCTYPE html>
<html lang="en">
<head>
<meta charset="utf-8">
<title>Brightwave Marketing – Banner Set</title>
<link rel="stylesheet" href="https://fonts.googleapis.com/css2?family=Roboto+Condensed:wght@400;700&family=Montserrat:wght@600&display=swap">
<style>
  :root {
    --page: #ffffff;
    --frame: #222222;
    --blue: #1b6fc8;
    --blue-deep: #0d4f9e;
    --blue-light: #3a8fe0;
    --navy: #0a3a78;
    --logo: #1d5ea8;
    --chip: #2a2a2e;
    --chip-edge: #55585e;
    --white: #ffffff;
    --ink: #1a1a1a;
    --device-dark: #1e1f24;
    --device-mid: #6b7077;
  }
  * { box-sizing: border-box; margin: 0; padding: 0; }
  html, body { width: 1200px; height: 755px; overflow: hidden; background: var(--page); }
  body { position: relative; font-family: "Roboto Condensed", "Arial Narrow", sans-serif; }

  .banner { position: absolute; border: 2px solid var(--frame); background: var(--white); overflow: hidden; }
  .banner--square { left: 355px; top: 24px; width: 482px; height: 404px; }
  .banner--leader { left: 13px; top: 450px; width: 1167px; height: 148px; }
  .banner--strip  { left: 13px; top: 613px; width: 752px; height: 98px; }

  .stage {
    position: absolute;
    background: radial-gradient(ellipse at 60% 40%, var(--blue-light) 0%, var(--blue) 45%, var(--blue-deep) 100%);
  }

  .brand { position: absolute; display: flex; align-items: center; gap: 8px; color: var(--logo); font-family: "Montserrat", sans-serif; font-weight: 600; }
  .brand__dot { background: var(--logo); border-radius: 50%; flex: none; }
  .brand__name { display: flex; flex-direction: column; line-height: 1; }
  .brand__sub { letter-spacing: 0.42em; }

  .headline {
    position: absolute; font-weight: 700; color: var(--white); text-align: center; line-height: 1.05; letter-spacing: -0.01em;
    text-shadow: 0 2px 3px rgba(0,0,0,0.55); white-space: nowrap;
  }

  .device { position: absolute; border-radius: 6px;
    background: linear-gradient(160deg, var(--device-mid) 0%, var(--device-dark) 55%, #3b3f46 100%); }

  .services { position: absolute; list-style: none; }
  .service {
    background: var(--chip); color: var(--white); border: 1px solid var(--chip-edge);
    display: flex; align-items: center; white-space: nowrap; overflow: hidden;
  }
  .service::before {
    content: ""; border-left: 0.55em solid var(--white); border-top: 0.33em solid transparent; border-bottom: 0.33em solid transparent;
    margin-right: 0.5em; flex: none;
  }

  .cta {
    position: absolute; background: var(--navy); color: var(--white); font-weight: 700; border: 1px solid #5f86c0;
    display: flex; align-items: center; justify-content: center; gap: 0.35em; letter-spacing: -0.01em;
  }
  .cta::after {
    content: ""; border-left: 0.45em solid var(--blue-light); border-top: 0.35em solid transparent; border-bottom: 0.35em solid transparent;
  }
  .site-url { position: absolute; color: var(--ink); font-family: Arial, Helvetica, sans-serif; text-align: center; white-space: nowrap; }

  /* 300x250 */
  .banner--square .brand { left: 0; right: 0; top: 16px; justify-content: center; }
  .banner--square .brand__dot { width: 12px; height: 12px; }
  .banner--square .brand__main { font-size: 30px; }
  .banner--square .brand__sub { font-size: 11px; margin-top: 3px; text-align: center; }
  .banner--square .stage { left: 0; top: 76px; width: 100%; height: 272px; }
  .banner--square .notch { position: absolute; left: 226px; top: 70px; }
  .banner--square .headline { left: 0; right: 0; top: 86px; font-size: 40px; }
  .banner--square .device { left: 8px; top: 184px; width: 262px; height: 172px; }
  .banner--square .services { left: 284px; top: 186px; width: 188px; }
  .banner--square .service { font-size: 18px; height: 26px; padding-left: 10px; margin-bottom: 4px; }
  .banner--square .service:nth-child(5) { font-size: 16px; }
  .banner--square .cta { left: 270px; top: 350px; width: 196px; height: 44px; font-size: 23px; }
  .banner--square .site-url { left: 20px; width: 240px; top: 364px; font-size: 17px; }

  /* 728x90 */
  .banner--leader .brand { left: 18px; top: 46px; }
  .banner--leader .brand__dot { width: 10px; height: 10px; }
  .banner--leader .brand__main { font-size: 23px; }
  .banner--leader .brand__sub { font-size: 9px; margin-top: 3px; }
  .banner--leader .stage { left: 250px; top: 0; width: 697px; height: 100%; }
  .banner--leader .notch { position: absolute; left: 250px; top: 56px; }
  .banner--leader .device { left: 264px; top: 10px; width: 258px; height: 126px; }
  .banner--leader .headline { left: 528px; width: 410px; top: 10px; font-size: 33px; }
  .banner--leader .services { left: 541px; top: 60px; width: 380px; display: grid; grid-template-columns: 180px 180px; gap: 5px 14px; }
  .banner--leader .service { font-size: 17px; height: 22px; padding-left: 8px; }
  .banner--leader .service--wide { grid-column: 1 / 3; justify-self: center; width: 180px; }
  .banner--leader .cta { left: 955px; top: 52px; width: 195px; height: 46px; font-size: 23px; }
  .banner--leader .site-url { left: 955px; width: 195px; top: 104px; font-size: 16px; }

  /* 480x60 */
  .banner--strip .brand { left: 12px; top: 28px; gap: 6px; }
  .banner--strip .brand__dot { width: 7px; height: 7px; }
  .banner--strip .brand__main { font-size: 17px; }
  .banner--strip .brand__sub { font-size: 7px; margin-top: 2px; }
  .banner--strip .stage { left: 206px; top: 0; width: 407px; height: 100%; }
  .banner--strip .device { left: 214px; top: 6px; width: 128px; height: 84px; }
  .banner--strip .headline { left: 342px; width: 262px; top: 5px; font-size: 20px; }
  .banner--strip .services { left: 349px; top: 35px; width: 250px; display: grid; grid-template-columns: 115px 115px; gap: 4px 14px; }
  .banner--strip .service { font-size: 11px; height: 15px; padding-left: 5px; }
  .banner--strip .service--wide { grid-column: 1 / 3; justify-self: center; width: 115px; }
  .banner--strip .cta { left: 623px; top: 30px; width: 120px; height: 30px; font-size: 15px; }
  .banner--strip .site-url { left: 618px; width: 130px; top: 67px; font-size: 10.5px; }
</style>
</head>
<body>

<section class="banner banner--square" aria-label="300 by 250 banner">
  <div class="brand">
    <span class="brand__dot"></span>
    <span class="brand__name"><span class="brand__main">BRIGHTWAVE</span><span class="brand__sub">MARKETING</span></span>
  </div>
  <div class="stage"></div>
  <svg class="notch" width="30" height="8" viewBox="0 0 30 8" aria-hidden="true"><polygon points="0,0 30,0 15,8" fill="#ffffff"/></svg>
  <h2 class="headline">We Drive Traffic &amp;<br>Phone Calls!</h2>
  <div class="device" role="img" aria-label="Responsive website shown on desktop monitor, tablet and phone"></div>
  <ul class="services">
    <li class="service">Web Design</li>
    <li class="service">Local SEO</li>
    <li class="service">Pay-Per-Click</li>
    <li class="service">Social Media</li>
    <li class="service">Content Marketing</li>
  </ul>
  <a class="cta">LEARN MORE</a>
  <span class="site-url">www.brightwavemktg.com</span>
</section>

<section class="banner banner--leader" aria-label="728 by 90 banner">
  <div class="brand">
    <span class="brand__dot"></span>
    <span class="brand__name"><span class="brand__main">BRIGHTWAVE</span><span class="brand__sub">MARKETING</span></span>
  </div>
  <div class="stage"></div>
  <svg class="notch" width="10" height="30" viewBox="0 0 10 30" aria-hidden="true"><polygon points="0,0 10,15 0,30" fill="#ffffff"/></svg>
  <div class="device" role="img" aria-label="Responsive website shown on desktop monitor, tablet and phone"></div>
  <h2 class="headline">We Drive Traffic &amp; Phone Calls!</h2>
  <ul class="services">
    <li class="service">Web Design</li>
    <li class="service">Local SEO</li>
    <li class="service">Pay-Per-Click</li>
    <li class="service">Social Media</li>
    <li class="service service--wide">Content Marketing</li>
  </ul>
  <a class="cta">LEARN MORE</a>
  <span class="site-url">www.brightwavemktg.com</span>
</section>

<section class="banner banner--strip" aria-label="480 by 60 banner">
  <div class="brand">
    <span class="brand__dot"></span>
    <span class="brand__name"><span class="brand__main">BRIGHTWAVE</span><span class="brand__sub">MARKETING</span></span>
  </div>
  <div class="stage"></div>
  <div class="device" role="img" aria-label="Responsive website shown on desktop monitor, tablet and phone"></div>
  <h2 class="headline">We Drive Traffic &amp; Phone Calls!</h2>
  <ul class="services">
    <li class="service">Web Design</li>
    <li class="service">Local SEO</li>
    <li class="service">Pay-Per-Click</li>
    <li class="service">Social Media</li>
    <li class="service service--wide">Content Marketing</li>
  </ul>
  <a class="cta">LEARN MORE</a>
  <span class="site-url">www.brightwavemktg.com</span>
</section>

</body>
</html>
```